"Small Lamps Shine Far Tonight" Teaching Series

16:9 design
Size: 64"x36" @ 300 dpi
Should include the title: Small Lamps Shine Far Tonight
and text subtly "Summer 2017"
Should include the church logo in a subtle way.
This artwork will be printed as a large banner but we will also adapt the artwork to be used in other formats like social media, a weekly bulletin, digital signage etc.
We are looking for a graphic that captures the message of the series: God has gifted people with a variety of gifts, abilities and resources to be used in service to Him.
We would like to see designs with bright jewel tones with a modern feel. Attached are examples of designs we like.
Overview of the series: God’s people are diverse: personalities, generations, gifts, abilities, career, resources, skills etc. Many people who are only briefly mentioned in the New Testament had a lasting impact because they used their God given gifts to serve. They opened their home, mentored others, prayed, gave generously, or served in practical ways. God uses all types of people and service for His glory. Some people think that their gifts are small, ordinary or that their work doesn’t matter. This is not the case in God’s eyes. Every person is empowered by God to use his/her gifts to service and that matters for impacting eternity. God has given us all we need to join him in His mission.

```html
<!DOCTYPE html>
<html lang="en">
<head>
<meta charset="utf-8">
<title>Small Lamps Shine Far Tonight – Summer 2017</title>
<link href="https://fonts.googleapis.com/css2?family=Poppins:wght@400;700&family=Source+Sans+3:wght@400&display=swap" rel="stylesheet">
<style>
  :root {
    --bg: #f3e8e1;
    --panel-red: rgba(240, 70, 70, 0.84);
    --title-white: #ffffff;
    --ink: #231f20;
    --teal: #0f7f73;
    --sky: #4fb6dc;
    --amber: #f0a01c;
    --red: #e01f2b;
    --plum: #3b1b3c;
    --blue: #2d53a6;
    --wash: rgba(255, 255, 255, 0.28);
  }
  html, body {
    margin: 0;
    padding: 0;
    width: 1200px;
    height: 676px;
    overflow: hidden;
    background: var(--bg);
  }
  .series-banner {
    position: relative;
    width: 1200px;
    height: 676px;
    overflow: hidden;
    background: var(--bg);
  }
  .portrait-tile {
    position: absolute;
    box-shadow: inset 0 0 0 1px rgba(255, 255, 255, 0.35);
  }
  .portrait-wash {
    position: absolute;
    inset: 0;
    background: var(--wash);
  }
  .title-panel {
    position: absolute;
    left: 310px;
    top: 143px;
    width: 578px;
    height: 329px;
    background: var(--panel-red);
  }
  .series-title {
    margin: 0;
    position: absolute;
    inset: 0;
    color: var(--title-white);
    font-family: "Poppins", sans-serif;
    text-align: center;
    text-transform: uppercase;
  }
  .title-line {
    position: absolute;
    left: 0;
    right: 0;
    display: block;
    white-space: nowrap;
    line-height: 1;
  }
  .title-line--top {
    top: 28px;
    font-size: 70px;
    font-weight: 400;
    letter-spacing: 0.01em;
  }
  .title-line--bold {
    top: 116px;
    font-size: 96px;
    font-weight: 700;
    letter-spacing: -0.01em;
  }
  .title-line--spaced {
    top: 232px;
    font-size: 80px;
    font-weight: 400;
    letter-spacing: 0.28em;
    padding-left: 0.28em;
  }
  .season-label {
    position: absolute;
    left: 437px;
    top: 484px;
    width: 340px;
    margin: 0;
    font-family: "Source Sans 3", sans-serif;
    font-size: 53px;
    font-weight: 400;
    color: var(--ink);
    letter-spacing: -0.005em;
    line-height: 1;
    white-space: nowrap;
  }
  .jewel-bars {
    position: absolute;
    left: 439px;
    top: 538px;
  }
</style>
</head>
<body>
<main class="series-banner">
  <div class="portrait-tile" role="img" aria-label="Portrait photo of a smiling woman with light windswept hair" style="left:0;top:0;width:160px;height:338px;background:linear-gradient(180deg,#e9d7bf 0%,#f1ddd0 35%,#e8c7b6 70%,#d9b9a4 100%);"><div class="portrait-wash"></div></div>
  <div class="portrait-tile" role="img" aria-label="Portrait photo of a young woman with dark hair and earphones" style="left:160px;top:0;width:88px;height:338px;background:linear-gradient(180deg,#5a4038 0%,#b98a72 30%,#a97b66 60%,#9a9096 85%,#8c8189 100%);"><div class="portrait-wash"></div></div>
  <div class="portrait-tile" role="img" aria-label="Portrait photo of a smiling woman with long dark hair" style="left:248px;top:0;width:197px;height:338px;background:linear-gradient(90deg,#f0d8c8 0%,#eccbb8 55%,#6b5148 80%,#4e3a34 100%);"><div class="portrait-wash"></div></div>
  <div class="portrait-tile" role="img" aria-label="Portrait photo of a woman in a colourful patterned headscarf" style="left:445px;top:0;width:227px;height:338px;background:linear-gradient(90deg,#6f8f7c 0%,#c7705f 18%,#e2b9a0 40%,#e6bfa7 75%,#c79a85 100%);"><div class="portrait-wash"></div></div>
  <div class="portrait-tile" role="img" aria-label="Portrait photo of a man wearing glasses" style="left:672px;top:0;width:123px;height:338px;background:linear-gradient(180deg,#efe0d4 0%,#e7cdbd 40%,#ddbfae 100%);"><div class="portrait-wash"></div></div>
  <div class="portrait-tile" role="img" aria-label="Portrait photo of an older man with glasses and a grey beard" style="left:795px;top:0;width:180px;height:338px;background:linear-gradient(180deg,#e4dcd6 0%,#d6b59f 30%,#c49b84 60%,#9d9089 85%,#7f7a7d 100%);"><div class="portrait-wash"></div></div>
  <div class="portrait-tile" role="img" aria-label="Close-up portrait photo of a young woman with dark hair" style="left:975px;top:0;width:225px;height:338px;background:linear-gradient(90deg,#4b3a36 0%,#f3ddd0 20%,#f6e4d8 60%,#efd3c3 100%);"><div class="portrait-wash"></div></div>

  <div class="portrait-tile" role="img" aria-label="Close-up portrait photo of a man with dark skin" style="left:0;top:338px;width:210px;height:338px;background:linear-gradient(180deg,#8a6a5c 0%,#a77f69 40%,#9a705c 75%,#b08774 100%);"><div class="portrait-wash"></div></div>
  <div class="portrait-tile" role="img" aria-label="Portrait photo of a smiling young woman with dark hair" style="left:210px;top:338px;width:205px;height:338px;background:linear-gradient(90deg,#f1ddd0 0%,#eed2c1 60%,#705850 90%,#5c463f 100%);"><div class="portrait-wash"></div></div>
  <div class="portrait-tile" role="img" aria-label="Portrait photo of a woman with blue eyes" style="left:415px;top:338px;width:197px;height:338px;background:linear-gradient(180deg,#d9c8c4 0%,#efdcd0 35%,#ecd2c2 100%);"><div class="portrait-wash"></div></div>
  <div class="portrait-tile" role="img" aria-label="Portrait photo of a smiling woman with brown hair" style="left:612px;top:338px;width:163px;height:338px;background:linear-gradient(180deg,#9a6a56 0%,#e6c2ae 35%,#efd3c2 70%,#e5c2ad 100%);"><div class="portrait-wash"></div></div>
  <div class="portrait-tile" role="img" aria-label="Portrait photo of a smiling young man with dark skin" style="left:775px;top:338px;width:103px;height:338px;background:linear-gradient(180deg,#6a4c40 0%,#5a3e34 45%,#6e5045 80%,#4a372f 100%);"><div class="portrait-wash"></div></div>
  <div class="portrait-tile" role="img" aria-label="Portrait photo of a smiling red-haired woman" style="left:878px;top:338px;width:167px;height:338px;background:linear-gradient(180deg,#c8704a 0%,#d98a62 25%,#efd0bd 55%,#eacbb7 80%,#6fb5a4 100%);"><div class="portrait-wash"></div></div>
  <div class="portrait-tile" role="img" aria-label="Portrait photo of a smiling woman with dark hair" style="left:1045px;top:338px;width:155px;height:338px;background:linear-gradient(180deg,#5c463e 0%,#d8ab92 30%,#e0b59d 70%,#c99a86 100%);"><div class="portrait-wash"></div></div>

  <section class="title-panel">
    <h1 class="series-title">
      <span class="title-line title-line--top">Small Lamps</span>
      <span class="title-line title-line--bold">Shine Far</span>
      <span class="title-line title-line--spaced">Tonight</span>
    </h1>
  </section>

  <p class="season-label">SUMMER 2017</p>

  <svg class="jewel-bars" width="314" height="13" viewBox="0 0 314 13" aria-hidden="true">
    <rect x="0" y="0" width="48" height="13" fill="var(--teal)"/>
    <rect x="53" y="0" width="48" height="13" fill="var(--sky)"/>
    <rect x="106" y="0" width="48" height="13" fill="var(--amber)"/>
    <rect x="159" y="0" width="48" height="13" fill="var(--red)"/>
    <rect x="212" y="0" width="48" height="13" fill="var(--plum)"/>
    <rect x="265" y="0" width="48" height="13" fill="var(--blue)"/>
  </svg>
</main>
</body>
</html>
```